The Drawer Sage needs a business card

The drawer sage is a lead generation service serving the Custom Closet industry.

Here is the basic card information:

The Drawer Sage
Gregory Tessman
Owner/CEO
Maplewood, NC
704-555-0183 Cell
Email: gtessman@TheDrawerSage.example

Additional information for the card:

"High quality, flat rate lead generation exclusively for the custom closet industry"

Bullet points for the back:

- Low fixed cost
- Easy to budget
- Guaranteed qualified Leeds
- Exclusivity per city

Logo attached, head shot attached. Photos of closet systems attached

```html
<!DOCTYPE html>
<html lang="en">
<head>
<meta charset="utf-8">
<title>The Drawer Sage – Business Card</title>
<link rel="stylesheet" href="https://fonts.googleapis.com/css2?family=EB+Garamond:ital,wght@0,400;0,600;1,400&display=swap">
<style>
  :root {
    --bg: #e6e7ea;
    --paper: #ffffff;
    --bronze: #9c5c2b;
    --bronze-light: #c9a27f;
    --ink: #4a4a4c;
    --slate: #5a5a5d;
    --slate-dark: #4b4b4e;
    --accent: #c9772f;
    --strip: #ffffff;
  }
  * { box-sizing: border-box; margin: 0; padding: 0; }
  html, body { width: 1200px; height: 800px; overflow: hidden; background: var(--bg); }
  body { font-family: "EB Garamond", Georgia, serif; color: var(--ink); position: relative; }

  .card {
    position: absolute;
    left: 320px;
    width: 560px;
    height: 320px;
    border-radius: 4px;
    box-shadow: 0 6px 18px rgba(0,0,0,0.12);
    overflow: hidden;
  }

  /* Front */
  .card--front { top: 50px; background: var(--paper); }
  .front__brand {
    position: absolute; left: 40px; top: 40px;
    display: flex; align-items: center; gap: 12px;
  }
  .brand__dot { width: 14px; height: 14px; border-radius: 50%; background: var(--bronze); }
  .brand__name { font-size: 34px; font-weight: 400; color: var(--bronze); letter-spacing: 0.5px; }
  .front__rule {
    position: absolute; left: 36px; top: 104px; width: 320px; height: 1px;
    background: var(--bronze-light);
  }
  .front__tagline {
    position: absolute; left: 40px; top: 118px; width: 270px;
    font-style: italic; font-size: 16px; line-height: 1.3; color: var(--bronze);
  }
  .front__portrait {
    position: absolute; right: 44px; top: 30px; width: 150px; height: 150px; border-radius: 50%;
    background: radial-gradient(circle at 50% 40%, #7a6a62 0%, #3a3d45 55%, #24262c 100%);
    border: 4px solid #d9d9dc;
  }
  .front__contact {
    position: absolute; right: 44px; bottom: 26px; text-align: right;
  }
  .contact__name { font-style: italic; font-size: 28px; color: var(--bronze); line-height: 1.1; }
  .contact__title { font-size: 15px; color: var(--ink); margin-bottom: 8px; }
  .contact__line { font-size: 14px; color: var(--ink); display: flex; justify-content: flex-end; align-items: center; gap: 6px; line-height: 1.5; }
  .contact__sep { color: var(--bronze-light); }
  .icon { width: 12px; height: 12px; fill: var(--accent); flex: none; }

  /* Back */
  .card--back {
    top: 430px;
    background: linear-gradient(180deg, var(--slate-dark) 0 30px, var(--slate) 30px);
  }
  .back__strip {
    position: absolute; left: 0; right: 0; top: 30px; height: 120px;
    background: var(--strip);
    display: flex; gap: 12px; padding: 12px 16px;
  }
  .back__photo { flex: 1; border-radius: 2px; }
  .back__photo--a { background: linear-gradient(135deg, #e9e4dc, #b9ada0); }
  .back__photo--b { background: linear-gradient(135deg, #7a4e30, #c6a27a); }
  .back__photo--c { background: linear-gradient(135deg, #f1efe9, #c7c2b8); }
  .back__photo--d { background: linear-gradient(135deg, #8a5a36, #d4b590); }
  .back__brand {
    position: absolute; left: 40px; top: 200px;
    display: flex; align-items: center; gap: 12px;
  }
  .back__brand .brand__dot { background: #ffffff; }
  .back__brand .brand__name { color: #ffffff; font-size: 32px; }
  .back__bullets {
    position: absolute; left: 330px; top: 178px; list-style: none;
  }
  .back__bullets li {
    color: #ffffff; font-size: 17px; line-height: 1.6;
    display: flex; align-items: center; gap: 10px;
  }
  .back__bullets li::before {
    content: ""; width: 7px; height: 7px; border-radius: 50%;
    border: 2px solid var(--accent);
  }
</style>
</head>
<body>

<section class="card card--front" aria-label="Business card front">
  <div class="front__brand">
    <span class="brand__dot"></span>
    <span class="brand__name">The Drawer Sage</span>
  </div>
  <div class="front__rule"></div>
  <p class="front__tagline">High Quality, Flat Rate Lead Generation Exclusively For The Custom Closet Industry</p>
  <div class="front__portrait" role="img" aria-label="Headshot of Gregory Tessman"></div>
  <div class="front__contact">
    <p class="contact__name">Gregory Tessman</p>
    <p class="contact__title">Owner/CEO</p>
    <p class="contact__line">
      Maplewood, NC
      <svg class="icon" viewBox="0 0 12 12" aria-hidden="true"><path d="M6 0a4 4 0 0 0-4 4c0 3 4 8 4 8s4-5 4-8a4 4 0 0 0-4-4zm0 5.5A1.5 1.5 0 1 1 6 2.5a1.5 1.5 0 0 1 0 3z"/></svg>
      <span class="contact__sep">|</span>
      704-555-0183
      <svg class="icon" viewBox="0 0 12 12" aria-hidden="true"><path d="M3 0h6a1 1 0 0 1 1 1v10a1 1 0 0 1-1 1H3a1 1 0 0 1-1-1V1a1 1 0 0 1 1-1zm0 1.5v8h6v-8z"/></svg>
    </p>
    <p class="contact__line">
      gtessman@TheDrawerSage.example
      <svg class="icon" viewBox="0 0 12 12" aria-hidden="true"><path d="M1 2.5h10v7H1zM1 2.5l5 4 5-4" stroke="#fff" stroke-width="0.8"/></svg>
    </p>
  </div>
</section>

<section class="card card--back" aria-label="Business card back">
  <div class="back__strip">
    <div class="back__photo back__photo--a" role="img" aria-label="White custom closet with shelving"></div>
    <div class="back__photo back__photo--b" role="img" aria-label="Walk-in closet with wood cabinetry"></div>
    <div class="back__photo back__photo--c" role="img" aria-label="Bright white closet system"></div>
    <div class="back__photo back__photo--d" role="img" aria-label="Wood closet with central island"></div>
  </div>
  <div class="back__brand">
    <span class="brand__dot"></span>
    <span class="brand__name">The Drawer Sage</span>
  </div>
  <ul class="back__bullets">
    <li>Low fixed cost</li>
    <li>Easy to budget</li>
    <li>Guaranteed qualified Leeds</li>
    <li>Exclusivity per city</li>
  </ul>
</section>

</body>
</html>
```